Business card por a urban DJ, up scale audience target

Need a sober design, modern, conservative colors but i can consider some options, y play rnb, hip hop, EDM and top40.

Business card for contact and personal info, double sided, use logo attrached please; im 42 so i need a card acording to my age an target audience.

Target Market(s)

Adult people, up scale audience

Industry/Entity Type

Music Download

Contact Information for Business Card

Cel (318) 5024471963 www.kelvarodun.com

Requirements
Must have
• open mind
Nice to have
• open mind
Should not have
• DJ

```html
<!DOCTYPE html>
<html lang="en">
<head>
<meta charset="utf-8">
<title>Kelva – Business Card</title>
<link href="https://fonts.googleapis.com/css2?family=Arimo:wght@400;700&display=swap" rel="stylesheet">
<style>
  :root {
    --backdrop: #2e2f31;
    --card-white: #ffffff;
    --card-black: #0d0d0d;
    --panel-black: #141414;
    --panel-sheen: #3a3a3a;
    --ink-dark: #0b0b0b;
    --ink-light: #f2f2f2;
    --ink-muted: #d6d6d6;
  }
  * { box-sizing: border-box; margin: 0; padding: 0; }
  html, body {
    width: 1200px;
    height: 950px;
    overflow: hidden;
    background: var(--backdrop);
    font-family: "Arimo", Arial, sans-serif;
  }
  .sheet {
    width: 1200px;
    height: 950px;
    display: flex;
    flex-direction: column;
    align-items: center;
    justify-content: center;
    gap: 40px;
  }
  .card {
    width: 760px;
    height: 434px;
    position: relative;
    overflow: hidden;
    box-shadow: 0 10px 30px rgba(0,0,0,0.45);
  }

  /* Front side */
  .card--front { background: var(--card-white); }
  .front__brand {
    position: absolute;
    left: 0;
    top: 0;
    width: 385px;
    height: 100%;
    display: flex;
    align-items: center;
    justify-content: center;
  }
  .brand-name {
    font-weight: 700;
    letter-spacing: 2px;
    line-height: 1;
  }
  .front__brand .brand-name {
    font-size: 74px;
    color: var(--ink-dark);
  }
  .front__panel {
    position: absolute;
    top: 24px;
    right: 24px;
    bottom: 24px;
    width: 352px;
    background:
      linear-gradient(100deg, var(--panel-black) 0%, var(--panel-sheen) 10%, var(--panel-black) 24%, #1c1c1c 60%, #262626 100%);
    display: flex;
    flex-direction: column;
    justify-content: center;
    padding-left: 100px;
    color: var(--ink-light);
  }
  .contact__name {
    font-size: 22px;
    font-weight: 700;
    letter-spacing: 0.5px;
  }
  .contact__role {
    font-size: 17px;
    font-weight: 400;
    color: var(--ink-muted);
    margin-top: 2px;
  }
  .contact__phone,
  .contact__web {
    font-size: 17px;
    font-weight: 400;
    color: var(--ink-muted);
  }
  .contact__phone { margin-top: 14px; }
  .contact__web { margin-top: 4px; }

  /* Back side */
  .card--back {
    background: linear-gradient(110deg, #050505 0%, var(--card-black) 50%, #1f1f1f 62%, var(--card-black) 75%);
    display: flex;
    flex-direction: column;
    align-items: center;
    justify-content: center;
    gap: 22px;
  }
  .card--back .brand-name {
    font-size: 96px;
    color: var(--ink-light);
  }
  .back__web {
    font-size: 18px;
    letter-spacing: 3px;
    color: var(--ink-muted);
  }
</style>
</head>
<body>
  <main class="sheet">
    <section class="card card--front" aria-label="Card front">
      <div class="front__brand">
        <span class="brand-name">KELVA</span>
      </div>
      <div class="front__panel">
        <p class="contact__name">MARCUS LENNE</p>
        <p class="contact__role">PRESIDENT</p>
        <p class="contact__phone">(318) 5024471963</p>
        <p class="contact__web">www.kelvarodun.com</p>
      </div>
    </section>

    <section class="card card--back" aria-label="Card back">
      <span class="brand-name">KELVA</span>
      <p class="back__web">KELVARODUN.COM</p>
    </section>
  </main>
</body>
</html>
```